SaaS Early tech startup business card design

Unique design for experience ecommerce platform company. the business cards will be used by executive members. conformance with color code is required.

```html
<!DOCTYPE html>
<html lang="en">
<head>
<meta charset="utf-8">
<title>Novix — Business Card</title>
<link href="https://fonts.googleapis.com/css2?family=Source+Sans+3:wght@400;600;700&display=swap" rel="stylesheet">
<style>
  :root {
    --brand-blue: #3b6990;
    --brand-teal: #67b99a;
    --ink: #1c1c1c;
    --paper: #ffffff;
    --backdrop: #3a3a3a;
  }
  * { margin: 0; padding: 0; box-sizing: border-box; }
  html, body {
    width: 1200px;
    height: 800px;
    overflow: hidden;
    background: var(--backdrop);
    font-family: "Source Sans 3", sans-serif;
  }
  .canvas {
    position: relative;
    width: 1200px;
    height: 800px;
  }
  .card {
    position: absolute;
    left: 315px;
    width: 570px;
    height: 329px;
    border-radius: 24px;
    overflow: hidden;
  }
  .card--front {
    top: 51px;
    background: var(--paper);
  }
  .card--back {
    top: 418px;
    background: var(--brand-blue);
  }
  .front__band {
    position: absolute;
    left: 0;
    right: 0;
    bottom: 0;
    height: 12px;
    background: var(--brand-blue);
  }
  .wordmark {
    position: absolute;
    font-weight: 700;
    line-height: 1;
    letter-spacing: -1px;
  }
  .wordmark--front {
    left: 48px;
    top: 208px;
    font-size: 76px;
    color: var(--brand-blue);
  }
  .wordmark--back {
    left: 0;
    right: 0;
    top: 82px;
    text-align: center;
    font-size: 176px;
    color: var(--brand-teal);
  }
  .identity {
    position: absolute;
    left: 290px;
    top: 61px;
  }
  .identity__name {
    font-size: 22px;
    font-weight: 700;
    color: var(--brand-blue);
    line-height: 1.1;
  }
  .identity__title {
    font-size: 13.5px;
    color: var(--ink);
    line-height: 1.1;
  }
  .identity__rule {
    width: 132px;
    height: 1.5px;
    margin-top: 8px;
    background: var(--brand-teal);
  }
  .contact {
    position: absolute;
    left: 290px;
    top: 201px;
    font-size: 13.5px;
    color: var(--ink);
    line-height: 1.25;
  }
  .contact__address { margin-bottom: 5px; }
  .contact__line {
    display: flex;
    align-items: center;
    gap: 6px;
    height: 17.5px;
  }
  .contact__icon {
    width: 9px;
    height: 9px;
    fill: var(--brand-blue);
    flex: none;
  }
</style>
</head>
<body>
<div class="canvas">
  <section class="card card--front">
    <div class="identity">
      <div class="identity__name">Dara Whitlow</div>
      <div class="identity__title">Managing Director</div>
      <div class="identity__rule"></div>
    </div>

    <div class="wordmark wordmark--front">novix</div>

    <div class="contact">
      <div class="contact__address">Your location street here,<br>Country name, Country - 91542</div>
      <div class="contact__line">
        <svg class="contact__icon" viewBox="0 0 10 10" aria-hidden="true"><path d="M2 0.5 L3.6 2.6 L2.8 3.6 Q4 6 6.4 7.2 L7.4 6.4 L9.5 8 L8.4 9.5 Q3.5 9 0.5 1.6 Z"/></svg>
        <span>+012 345 6789</span>
      </div>
      <div class="contact__line">
        <svg class="contact__icon" viewBox="0 0 10 10" aria-hidden="true"><path d="M0 2 H10 V8.5 H0 Z M0.6 2.4 L5 5.8 L9.4 2.4" stroke="#fff" stroke-width="0.8"/></svg>
        <span>info@youremail.com</span>
      </div>
      <div class="contact__line">
        <svg class="contact__icon" viewBox="0 0 10 10" aria-hidden="true"><circle cx="5" cy="5" r="4.8"/><path d="M2.5 2.5 Q4 3 3.5 4.5 Q5 5.5 4 7.5 M6 1.2 Q7 3 8.5 3.5 M6 6 Q7.5 6.5 7.5 8.5" stroke="#fff" stroke-width="0.8" fill="none"/></svg>
        <span>www.yourwebsite.com</span>
      </div>
    </div>

    <div class="front__band"></div>
  </section>

  <section class="card card--back">
    <div class="wordmark wordmark--back">novix</div>
  </section>
</div>
</body>
</html>
```